Lantern Hearthworks Business Cards

Looking to create simple business cards that highlight our unique three sided triangle fire pit design with the colors and font of our logo, listed below.

Requirements
Must have
• Looking for something simple that includes a picture of our fire pit with name, website (lanternhearthworks.com), phone number and email. Want to keep the color mostly orange and black.
• Font is gotham(medium) and orange color code is #ee6e22

```html
<!DOCTYPE html>
<html lang="en">
<head>
<meta charset="utf-8">
<title>Lantern Hearthworks Business Cards</title>
<link rel="stylesheet" href="https://fonts.googleapis.com/css2?family=Montserrat:wght@400;500;600&display=swap">
<style>
  :root {
    --orange: #ee6e22;
    --charcoal: #262626;
    --ink-grey: #5f5f5f;
    --rule-grey: #9a9a9a;
    --paper: #f6f6f6;
    --backdrop: #9c9c9c;
    --white: #ffffff;
  }
  * { margin: 0; padding: 0; box-sizing: border-box; }
  html, body {
    width: 1200px;
    height: 1048px;
    overflow: hidden;
  }
  body {
    background: var(--backdrop);
    font-family: "Montserrat", sans-serif;
    position: relative;
  }
  .card {
    position: absolute;
    left: 288px;
    width: 625px;
    height: 358px;
    overflow: hidden;
  }
  .card-front { top: 144px; background: var(--paper); }
  .card-back {
    top: 547px;
    background: radial-gradient(ellipse at 50% 40%, #3a3a3a 0%, #2a2a2a 55%, #1e1e1e 100%);
    display: flex;
    align-items: center;
    justify-content: center;
  }

  .front-info {
    position: absolute;
    left: 0; top: 0;
    width: 349px; height: 100%;
  }
  .brand-name {
    position: absolute;
    left: 42px; top: 60px;
    color: var(--orange);
    font-weight: 500;
    font-size: 22px;
    line-height: 1.1;
    letter-spacing: 0.2em;
    text-transform: uppercase;
  }
  .person-name {
    position: absolute;
    left: 41px; top: 204px;
    font-size: 19px;
    font-weight: 600;
    letter-spacing: 0.02em;
    color: var(--orange);
  }
  .person-name .surname { color: var(--ink-grey); }
  .contact {
    position: absolute;
    left: 41px; top: 248px;
    font-size: 14px;
    line-height: 17px;
    color: var(--ink-grey);
  }
  .website {
    position: absolute;
    left: 41px; top: 298px;
    font-size: 14px;
    color: var(--ink-grey);
  }
  .website strong { color: var(--orange); font-weight: 600; }

  .accent-rule {
    position: absolute;
    left: 349px; top: 0;
    width: 4px; height: 100%;
    background: var(--orange);
  }
  .product-photo {
    position: absolute;
    left: 353px; top: 0;
    width: 272px; height: 100%;
    background:
      radial-gradient(circle at 60% 48%, rgba(238,110,34,0.85) 0%, rgba(190,70,20,0.45) 18%, rgba(20,20,20,0) 38%),
      linear-gradient(160deg, #2e2e2e 0%, #1f1f1f 100%);
  }

  .back-brand {
    display: flex;
    flex-direction: column;
    align-items: center;
    gap: 22px;
  }
  .back-dot {
    width: 18px;
    height: 18px;
    border-radius: 50%;
    background: var(--orange);
  }
  .back-name {
    color: var(--white);
    font-weight: 500;
    font-size: 30px;
    letter-spacing: 0.22em;
    text-transform: uppercase;
    padding-left: 0.22em;
  }
</style>
</head>
<body>
  <section class="card card-front">
    <div class="front-info">
      <p class="brand-name">Lantern<br>Hearthworks</p>
      <p class="person-name">DALE <span class="surname">MORROW</span></p>
      <p class="contact">503-555-0187<br>dale.m@lanternhearthworks.com</p>
      <p class="website">www.<strong>lanternhearthworks</strong>.com</p>
    </div>
    <div class="accent-rule"></div>
    <div class="product-photo" role="img" aria-label="Photo from above of a triangular steel fire pit with burning logs and bright orange flames on dark gravel"></div>
  </section>

  <section class="card card-back">
    <div class="back-brand">
      <span class="back-dot"></span>
      <p class="back-name">Lantern Hearthworks</p>
    </div>
  </section>
</body>
</html>
```